Poster Design For Obstacle Run

Design a poster for the Crow Ridge Obstacle run.
Text: Crow Ridge Obstacle Run. May 12th, 2018. Kraaiveld. www.crowridgedash.nl. I have added a lot of pictures.
Furthermore, the logo should be included. As an example I included a poster from the ironbark race that we really like (ironbark team challenge) and also. Feel free to take a look at our website for inspiration: www.crowridgedash.nl

```html
<!DOCTYPE html>
<html lang="en">
<head>
<meta charset="utf-8">
<title>Crow Ridge Obstacle Run</title>
<link href="https://fonts.googleapis.com/css2?family=Bebas+Neue&family=Oswald:wght@400;500&display=swap" rel="stylesheet">
<style>
  :root {
    --mud-dark: #2a2620;
    --mud-mid: #5e574c;
    --mud-light: #8c8476;
    --ink-white: #f4f2ee;
    --accent-orange: #e2542a;
  }
  * { margin: 0; padding: 0; box-sizing: border-box; }
  html, body {
    width: 874px;
    height: 1200px;
    overflow: hidden;
    background: var(--mud-dark);
  }
  .poster {
    position: relative;
    width: 874px;
    height: 1200px;
    overflow: hidden;
    font-family: "Oswald", sans-serif;
    color: var(--ink-white);
  }
  .hero-photo {
    position: absolute;
    inset: 0;
    background:
      radial-gradient(ellipse 70% 45% at 55% 55%, rgba(150,140,124,0.55), transparent 70%),
      radial-gradient(ellipse 50% 30% at 30% 85%, rgba(120,112,98,0.5), transparent 70%),
      linear-gradient(180deg, #3a352e 0%, var(--mud-mid) 30%, var(--mud-light) 55%, var(--mud-mid) 78%, var(--mud-dark) 100%);
  }
  .hero-photo::after {
    content: "";
    position: absolute;
    inset: 0;
    background: linear-gradient(180deg, rgba(0,0,0,0.25) 0%, transparent 25%, transparent 70%, rgba(0,0,0,0.55) 100%);
  }
  .title {
    position: absolute;
    left: 0;
    right: 0;
    top: 205px;
    text-align: center;
    font-family: "Bebas Neue", sans-serif;
    font-weight: 400;
    line-height: 1;
    text-shadow: 0 2px 10px rgba(0,0,0,0.35);
  }
  .title-name {
    display: block;
    font-size: 182px;
    letter-spacing: 2px;
  }
  .title-event {
    display: block;
    margin-top: 36px;
    font-size: 150px;
    letter-spacing: 1px;
  }
  .title-event .accent { color: var(--accent-orange); }
  .date-band {
    position: absolute;
    left: 180px;
    top: 604px;
    width: 514px;
    height: 78px;
    background: var(--accent-orange);
    display: flex;
    align-items: center;
    justify-content: center;
    font-size: 38px;
    font-weight: 500;
    letter-spacing: 4px;
  }
  .brand-mark {
    position: absolute;
    left: 28px;
    bottom: 38px;
    display: flex;
    align-items: center;
    gap: 12px;
  }
  .brand-mark .dot {
    width: 30px;
    height: 30px;
    border-radius: 50%;
    background: var(--accent-orange);
  }
  .brand-mark .brand-name {
    font-family: "Bebas Neue", sans-serif;
    font-size: 38px;
    letter-spacing: 1px;
    color: var(--ink-white);
  }
  .event-details {
    position: absolute;
    left: 280px;
    width: 340px;
    bottom: 44px;
    text-align: center;
    line-height: 1;
  }
  .event-city {
    font-size: 28px;
    letter-spacing: 7px;
    font-weight: 500;
  }
  .event-site {
    margin-top: 20px;
    font-size: 28px;
    letter-spacing: 3px;
    font-weight: 400;
  }
</style>
</head>
<body>
  <main class="poster">
    <div class="hero-photo" role="img" aria-label="Close-up of a runner's legs splashing through a muddy puddle"></div>

    <h1 class="title">
      <span class="title-name">CROW RIDGE</span>
      <span class="title-event">OBSTACLE<span class="accent">RUN</span></span>
    </h1>

    <div class="date-band">MAY 12TH, 2018</div>

    <div class="brand-mark">
      <span class="dot"></span>
      <span class="brand-name">CROW RIDGE</span>
    </div>

    <div class="event-details">
      <p class="event-city">KRAAIVELD</p>
      <p class="event-site">www.crowridgedash.nl</p>
    </div>
  </main>
</body>
</html>
```